Minimalist theatrical poster for the film

Create a poster, using some of the attached images for inspiration. Please match the font of the teaser poster for the title (The Bluewater) and leave space at the bottom for the credits block, which I will add later. Any characters presented on the poster should resemble the actors in the film, and not be clip art. The movie is about Owen, a 14 year old in the summer of 2001, and his first love (Greta). As he falls for her, he lets himself still be distracted by his good friend Maisie, eventually causing trouble in his relationships with Greta, Maisie, and best friend Theo. Trailer is included in the files below! Extra credit for a good marketing tag along the lines of "remember your first love" or something about the film being a romantic comedy adventure etc.

```html
<!DOCTYPE html>
<html lang="en">
<head>
<meta charset="utf-8">
<title>Owen &amp; The Bluewater — Poster</title>
<link rel="stylesheet" href="https://fonts.googleapis.com/css2?family=Kaushan+Script&family=Oswald:wght@500&display=swap">
<style>
  :root {
    --page-bg: #e9e8e6;
    --sky-light: #eef6fd;
    --sky-mid: #b4d9f4;
    --sky-deep: #8ec4ec;
    --ink: #111111;
    --bokeh: rgba(255, 255, 255, 0.55);
    --silhouette-top: #2a3440;
    --silhouette-bottom: #151a20;
  }
  html, body {
    margin: 0;
    padding: 0;
    width: 1200px;
    height: 1148px;
    overflow: hidden;
    background: var(--page-bg);
  }
  .poster {
    position: absolute;
    left: 270px;
    top: 34px;
    width: 660px;
    height: 1080px;
    overflow: hidden;
    background: radial-gradient(ellipse 70% 45% at 50% 82%, var(--sky-light) 0%, var(--sky-mid) 55%, var(--sky-deep) 100%);
    box-shadow: 0 2px 10px rgba(0, 0, 0, 0.12);
  }
  .bokeh {
    position: absolute;
    inset: 0;
  }
  .swing-art {
    position: absolute;
    left: 180px;
    top: 0;
    width: 300px;
    height: 530px;
    border-radius: 0 0 40px 40px;
    background: linear-gradient(180deg, var(--silhouette-top) 0%, var(--silhouette-bottom) 100%);
    opacity: 0.88;
  }
  .title {
    position: absolute;
    left: 0;
    right: 0;
    top: 560px;
    margin: 0;
    text-align: center;
    font-family: "Kaushan Script", cursive;
    font-weight: 400;
    color: var(--ink);
    line-height: 1;
  }
  .title-lead {
    display: block;
    font-size: 128px;
    transform: translateX(-18px);
  }
  .title-join {
    display: block;
    font-size: 74px;
    margin-top: -14px;
    transform: translateX(40px);
  }
  .title-join .amp {
    font-size: 34px;
    vertical-align: top;
    margin-right: 10px;
  }
  .title-tail {
    display: block;
    font-size: 118px;
    margin-top: -4px;
  }
  .credits {
    position: absolute;
    left: 0;
    right: 0;
    top: 940px;
    text-align: center;
    font-family: "Oswald", sans-serif;
    font-weight: 500;
    color: var(--ink);
    text-transform: uppercase;
    letter-spacing: 0.2px;
  }
  .credits p {
    margin: 0 0 4px;
    line-height: 1.15;
  }
  .credits-presents { font-size: 12px; }
  .credits-presents small { font-size: 6px; margin: 0 4px; }
  .credits-cast { font-size: 12.5px; }
  .credits-crew { font-size: 12px; }
  .credits-crew .role {
    display: inline-block;
    font-size: 5px;
    line-height: 1.1;
    text-align: right;
    vertical-align: middle;
    margin-right: 6px;
  }
</style>
</head>
<body>
  <main class="poster">
    <svg class="bokeh" width="660" height="1080" viewBox="0 0 660 1080" aria-hidden="true">
      <g fill="var(--bokeh)">
        <circle cx="123" cy="214" r="13"/>
        <circle cx="77" cy="395" r="12"/>
        <circle cx="188" cy="451" r="10"/>
        <circle cx="555" cy="386" r="25"/>
        <circle cx="484" cy="342" r="9"/>
        <circle cx="505" cy="524" r="17"/>
        <circle cx="180" cy="600" r="8"/>
        <circle cx="455" cy="663" r="9"/>
        <circle cx="560" cy="718" r="20"/>
        <circle cx="188" cy="720" r="6"/>
        <circle cx="305" cy="470" r="9"/>
        <circle cx="360" cy="350" r="7"/>
        <circle cx="280" cy="826" r="14"/>
        <circle cx="545" cy="560" r="7"/>
      </g>
    </svg>

    <div class="swing-art" role="img" aria-label="Silhouettes of a boy in a cap and a girl on two playground swings hanging from chains, holding hands"></div>

    <h1 class="title">
      <span class="title-lead">Owen</span>
      <span class="title-join"><span class="amp">&amp;</span>The</span>
      <span class="title-tail">Bluewater</span>
    </h1>

    <footer class="credits">
      <p class="credits-presents">Harborline Pictures <small>presents</small> "Owen &amp; The Bluewater"</p>
      <p class="credits-cast">Rory Kessler Lena Gottfried Andrew Galvano Kayla Morrow Adeline Hart and Sean Whitmore</p>
      <p class="credits-crew"><span class="role">written by<br>directed by</span>Jonah Wexley</p>
    </footer>
  </main>
</body>
</html>
```